Looking for a high-end business card design for a construction company

We are looking to update our business card design. We are a post-frame construction company that builds custom buildings, commercial spaces, homes, and anything else. We have multiple people working here so we would need something we can easily customize the information for the specific person. We need a name, website, cell phone, office phone as well as social icons. Our colors are black, white, and grey/silver so I would love a black background or something that is more striking than just a traditional white business card. Looking for something that is very professional with a high-end look/feel. I have attached our logos, they can be silver, white, grey, or black.
Industry/Entity Type
Construction
Contact Information for Business Card
Business logo, Name, Cell phone, Office phone, website, social Icons
Colors
Designer to choose only greyscale colors for use in the design.
Look and feel

```html
<!DOCTYPE html>
<html lang="en">
<head>
<meta charset="utf-8">
<title>Kestrel Builders – Business Card</title>
<link rel="stylesheet" href="https://fonts.googleapis.com/css2?family=Arimo:wght@400;700&display=swap">
<style>
  :root{
    --page:#ffffff;
    --card:#1b1b1b;
    --card-edge:#222222;
    --silver:#d2d2d2;
    --silver-soft:#a9a9a9;
    --grey:#7d7d7d;
    --icon:#8c8c8c;
  }
  *{margin:0;padding:0;box-sizing:border-box}
  html,body{width:1200px;height:1200px;overflow:hidden;background:var(--page)}
  body{position:relative;font-family:"Arimo",Arial,sans-serif}
  .card{
    position:absolute;left:199px;width:810px;height:462px;
    background:radial-gradient(ellipse at 40% 20%,var(--card-edge),var(--card) 70%);
  }
  .card--front{top:100px}
  .card--back{top:646px}

  .person-name{
    position:absolute;left:56px;top:80px;
    font-size:33px;font-weight:700;letter-spacing:.09em;color:var(--silver);
    text-transform:uppercase;white-space:nowrap;
  }
  .person-name .surname{font-weight:400}
  .person-title{
    position:absolute;left:56px;top:130px;
    font-size:21px;letter-spacing:.12em;color:var(--silver-soft);text-transform:uppercase;
  }
  .divider{position:absolute;left:56px;top:194px;width:704px;height:2px;background:var(--grey)}
  .divider::before{content:"";position:absolute;left:0;top:-2px;width:232px;height:5px;background:var(--grey)}

  .contact-list{position:absolute;left:56px;top:248px;list-style:none}
  .contact-item{
    display:flex;align-items:center;height:32.5px;
    font-size:20px;letter-spacing:.14em;color:var(--silver);white-space:nowrap;
  }
  .contact-item svg{width:22px;height:22px;margin-right:14px;flex:none}
  .social-list{position:absolute;left:56px;top:388px;display:flex;gap:16px}
  .social-dot{width:34px;height:34px;border-radius:50%;background:var(--icon)}

  .brand{position:absolute;text-align:center;color:var(--silver);font-weight:700;line-height:1;text-transform:uppercase}
  .brand--front{left:480px;top:366px;width:290px}
  .brand--front .brand-name{font-size:36px;letter-spacing:.16em}
  .brand--front .brand-sub{font-size:18px;letter-spacing:.18em;margin-top:6px}
  .brand--back{left:0;top:264px;width:810px}
  .brand--back .brand-name{font-size:58px;letter-spacing:.16em}
  .brand--back .brand-sub{font-size:30px;letter-spacing:.16em;margin-top:10px}

  .back-web{
    position:absolute;left:0;top:389px;width:810px;text-align:center;
    font-size:25px;letter-spacing:.5em;color:var(--silver-soft);
  }
</style>
</head>
<body>

<section class="card card--front">
  <h1 class="person-name">Marcus <span class="surname">Delaney</span></h1>
  <p class="person-title">Founder</p>
  <div class="divider"></div>

  <ul class="contact-list">
    <li class="contact-item">
      <svg viewBox="0 0 22 22" aria-hidden="true"><circle cx="11" cy="11" r="11" fill="var(--icon)"/><rect x="7.5" y="4.5" width="7" height="13" rx="1.5" fill="none" stroke="#1b1b1b" stroke-width="1.4"/></svg>
      555 201 4478
    </li>
    <li class="contact-item">
      <svg viewBox="0 0 22 22" aria-hidden="true"><circle cx="11" cy="11" r="11" fill="var(--icon)"/><path d="M7 5.5c1-.6 1.8.2 2.3 1.3l.5 1.2c.2.6-.3 1.1-.8 1.5.6 1.4 1.6 2.4 3 3 .4-.5.9-1 1.5-.8l1.2.5c1.1.5 1.9 1.3 1.3 2.3-.8 1.3-2.4 1.600-4 .9-2.6-1.1-4.7-3.2-5.8-5.8-.7-1.6-.4-3.2.8-4.1z" fill="#1b1b1b"/></svg>
      5550 201 440
    </li>
    <li class="contact-item">
      <svg viewBox="0 0 22 22" aria-hidden="true"><rect x="1" y="5" width="20" height="13" rx="1" fill="var(--icon)"/><path d="M1.5 5.5 11 12.5l9.5-7" fill="none" stroke="#1b1b1b" stroke-width="1.4"/></svg>
      info@kestrelbuilders.com
    </li>
    <li class="contact-item">
      <svg viewBox="0 0 22 22" aria-hidden="true" fill="none" stroke="var(--icon)" stroke-width="1.5"><circle cx="11" cy="11" r="9.5"/><ellipse cx="11" cy="11" rx="4.2" ry="9.5"/><path d="M1.5 11h19M3 6h16M3 16h16"/></svg>
      www.kestrelbuilders.com
    </li>
  </ul>

  <div class="social-list">
    <span class="social-dot" role="img" aria-label="Social profile one"></span>
    <span class="social-dot" role="img" aria-label="Social profile two"></span>
    <span class="social-dot" role="img" aria-label="Social profile three"></span>
  </div>

  <div class="brand brand--front">
    <div class="brand-name">Kestrel</div>
    <div class="brand-sub">Builders, Inc.</div>
  </div>
</section>

<section class="card card--back">
  <div class="brand brand--back">
    <div class="brand-name">Kestrel</div>
    <div class="brand-sub">Builders, Inc.</div>
  </div>
  <p class="back-web">www.kestrelbuilders.com</p>
</section>

</body>
</html>
```